Simple, bright, clean website - 3 pages, easy to update with WordPress!

I want to update my website (brevatlo.com) with a brighter/cleaner interface. It is quite dark right now. I would like it to be similar to a partner site (https://www.velmo-482.com/). White with some orange highlights (matching the logo). I want to be able to easily update the site content. There should be 3 main pages: About, Services, Contact. I also like a design similar to tarnop.com

Target Market(s)

Anyone using technology to achieve business goals.

Industry/Entity Type

Managed Service Provider (IT)

Coding

Coded - Design and coding required

Number of Pages Required

3 page

Colors
F0912C
F2A743
F7CA91
FBE8D2
FDF5EE

Requirements
Must have
• Links to standard social media apps like LinkedIn, Facebook, etc.. Easy to edit and add pages.

```html
<!DOCTYPE html>
<html lang="en">
<head>
<meta charset="utf-8">
<title>Brevatlo Consulting Inc</title>
<link href="https://fonts.googleapis.com/css2?family=Montserrat:wght@300;400;500;600;700&display=swap" rel="stylesheet">
<style>
:root{
  --orange:#F0912C;
  --orange-2:#F2A743;
  --orange-3:#F7CA91;
  --orange-4:#FBE8D2;
  --cream:#FDF5EE;
  --amber:#F9A51B;
  --deep:#F06A0E;
  --ink:#1F1F1F;
  --dark:#262626;
  --text:#2b2b2b;
  --white:#ffffff;
}
*{margin:0;padding:0;box-sizing:border-box}
html,body{width:1200px;height:3753px;overflow:hidden}
body{font-family:"Montserrat",sans-serif;color:var(--text);background:var(--white);position:relative}
.abs{position:absolute}
.bg{position:absolute;left:0;top:0;width:1200px;height:3753px}
.nav a{position:absolute;top:52px;font-size:13px;color:var(--text);text-decoration:none}
.wordmark{font-weight:300;letter-spacing:2px;color:#555;text-align:center;line-height:1}
.wordmark small{display:block;font-size:11px;letter-spacing:6px;margin-top:2px}
.btn{position:absolute;display:flex;align-items:center;justify-content:center;font-size:12.5px;font-weight:700;border-radius:3px;text-decoration:none}
.btn::after{content:"";position:absolute;right:-3px;bottom:-3px;width:6px;height:6px;border-radius:50%;background:var(--orange)}
.btn-dark{background:var(--ink);color:var(--white)}
.btn-orange{background:var(--amber);color:var(--white)}
.btn-orange::after{background:var(--ink)}
.hero-title{left:189px;top:182px;font-size:47px;font-weight:300;line-height:50px;color:var(--ink)}
.hero-title em{font-style:normal;color:var(--amber)}
.para{font-size:12px;line-height:24px;color:var(--text)}
.photo{position:absolute}
.chev{position:absolute;width:40px;height:40px;border-radius:50%;border:1.5px solid var(--orange-2);background:var(--white);display:flex;align-items:center;justify-content:center}
.quote{left:188px;top:1358px;width:824px;height:148px;border:2px solid var(--orange-3);border-radius:14px;background:linear-gradient(90deg,#f4f4f4,#fff);text-align:center;font-size:29px;font-weight:300;line-height:38px;padding-top:35px;color:var(--ink)}
.quote b{font-weight:500}
.section-title{left:0;width:1200px;text-align:center;font-size:49px;font-weight:300;color:var(--ink)}
.section-title em{font-style:normal;color:var(--amber)}
.card{position:absolute;width:262px;height:328px;border:2px solid var(--orange-4);border-radius:12px;background:linear-gradient(180deg,#fffaf2,#fffdf9);text-align:center;padding:40px 30px 0}
.card.featured{background:linear-gradient(135deg,var(--deep),#FBB021);border-color:transparent;color:var(--white)}
.card h3{font-size:12.5px;font-weight:700;margin:20px -10px 8px;color:var(--ink)}
.card p{font-size:12px;line-height:24px}
.card.featured h3,.card.featured p{color:var(--white)}
.res{position:absolute;top:2904px;width:262px;height:323px;background:var(--cream);border-radius:8px;padding:12px}
.res .img{height:172px;border-radius:4px}
.res .date{font-size:12px;margin:26px 0 10px 10px}
.res h4{font-size:14px;font-weight:700;line-height:24px;margin-left:10px;color:var(--ink)}
.res .arrow{margin:10px 0 0 10px}
.foot h5{position:absolute;font-size:18px;font-weight:600;color:var(--white)}
.foot .line{position:absolute;font-size:12.5px;color:var(--white)}
.social{position:absolute;top:3582px;width:36px;height:36px;border-radius:50%;border:1.5px solid #555}
</style>
</head>
<body>

<svg class="bg" viewBox="0 0 1200 3753" aria-hidden="true">
  <defs>
    <linearGradient id="heroGrad" x1="0" y1="0" x2="1" y2="1">
      <stop offset="0" stop-color="#F4F6DF"/>
      <stop offset="0.45" stop-color="#FEF4E2"/>
      <stop offset="1" stop-color="#F8B866"/>
    </linearGradient>
    <linearGradient id="servGrad" x1="0" y1="0" x2="0" y2="1">
      <stop offset="0" stop-color="#F8C088"/>
      <stop offset="0.35" stop-color="#FDF2E4"/>
      <stop offset="1" stop-color="#FFFDF8"/>
    </linearGradient>
  </defs>
  <path d="M15 15 H1186 V640 Q1186 700 1128 706 L78 765 Q15 768 15 705 Z" fill="url(#heroGrad)"/>
  <path d="M15 1720 Q15 1666 78 1660 L1108 1600 Q1186 1596 1186 1670 V2800 H15 Z" fill="url(#servGrad)"/>
  <path d="M15 2872 Q15 2816 80 2810 L1110 2710 Q1186 2705 1186 2780 V3470 H15 Z" fill="var(--amber)"/>
  <path d="M0 3510 Q0 3456 62 3450 L1120 3378 Q1200 3374 1200 3420 V3753 H0 Z" fill="var(--dark)"/>
</svg>

<!-- Navigation -->
<nav class="nav">
  <a style="left:186px" href="#">About</a>
  <span class="abs" style="left:276px;top:56px;width:11px;height:11px;border:1px solid var(--orange-2);border-radius:50%"></span>
  <a style="left:336px" href="#">Services</a>
  <div class="abs wordmark" style="left:480px;top:36px;width:240px;font-size:40px">brevatlo<small>consulting inc.</small></div>
  <a style="left:775px" href="#">Resources</a>
  <a class="btn btn-orange" style="left:921px;top:41px;width:157px;height:38px;color:#fff" href="#">Contact Us</a>
</nav>

<!-- Hero -->
<h1 class="abs hero-title">Business<br>Momentum Starts<br>With <em>Simplified IT</em><br><em>Excellence.</em></h1>
<p class="abs para" style="left:188px;top:402px;width:410px">Brevatlo knows that a business builds its foundation with information and communication. You need the right technology to succeed in today's world. We establish long term partnerships with our clients to deliver operational efficiencies, reduce complexities and increase productivity.</p>
<a class="btn btn-dark" style="left:188px;top:555px;width:157px;height:39px" href="#">Contact Us</a>
<div class="photo" role="img" aria-label="Photo of two colleagues talking in a bright office" style="left:677px;top:146px;width:362px;height:454px;border-radius:30px;background:linear-gradient(160deg,#eef2f5,#c9ced3 55%,#8d8f93)"></div>
<div class="chev" style="left:580px;top:720px"><svg width="14" height="10" viewBox="0 0 14 10"><path d="M2 2l5 5 5-5" fill="none" stroke="var(--orange)" stroke-width="2.4"/></svg></div>

<!-- About -->
<div class="photo" role="img" aria-label="Photo of a smiling woman on the phone" style="left:188px;top:843px;width:392px;height:419px;background:linear-gradient(150deg,#f2efec,#d8c9bc 60%,#b69a82)"></div>
<span class="abs" style="left:507px;top:1191px;width:88px;height:88px;border-radius:50%;background:var(--white)"></span>
<div class="abs wordmark" style="left:690px;top:886px;width:270px;font-size:54px;text-align:left">brevatlo<small style="font-size:12px;padding-left:80px">consulting inc.</small></div>
<p class="abs para" style="left:690px;top:976px;width:330px">Brevatlo knows that a business builds its foundation with information and communication. You need the right technology to succeed in today's world. We establish long term partnerships with our clients to deliver operational efficiencies, reduce complexities and increase productivity.</p>
<a class="btn btn-orange" style="left:690px;top:1154px;width:158px;height:38px" href="#">Read more</a>

<div class="abs quote"><b>Brevatlo</b> understands that technology is a tool to<br>improve your business productivity.</div>

<div class="chev" style="left:580px;top:1609px"><svg width="14" height="10" viewBox="0 0 14 10"><path d="M2 2l5 5 5-5" fill="none" stroke="var(--orange)" stroke-width="2.4"/></svg></div>

<!-- Services -->
<h2 class="abs section-title" style="top:1700px">Our <em>Services</em></h2>
<p class="abs para" style="left:320px;top:1774px;width:560px;text-align:center">Brevatlo's services are focused on the needs of small and medium sized businesses. We specialize in the entire range of IT consulting including managed services and technical projects. Please visit the Services page for details.</p>

<div class="card" style="left:188px;top:1887px">
  <svg width="48" height="48" viewBox="0 0 48 48"><circle cx="22" cy="22" r="10" fill="none" stroke="var(--orange)" stroke-width="6" stroke-dasharray="5 3"/><circle cx="22" cy="22" r="5" fill="none" stroke="var(--orange)" stroke-width="3"/><path d="M26 34l6 6 12-14" fill="none" stroke="var(--orange)" stroke-width="4"/></svg>
  <h3>Installation &amp; Deployment</h3>
  <p>Lorem Ipsum is simply dummy text of the printing and typesetting industry. Lorem Ipsum has been the industry's standard dummy text ever since the 1500s</p>
</div>
<div class="card featured" style="left:469px;top:1887px">
  <svg width="48" height="48" viewBox="0 0 48 48"><path d="M10 28v-6a14 14 0 0128 0v6" fill="none" stroke="#fff" stroke-width="3.5"/><rect x="6" y="24" width="8" height="12" rx="3" fill="#fff"/><rect x="34" y="24" width="8" height="12" rx="3" fill="#fff"/><path d="M38 36q0 6-10 6" fill="none" stroke="#fff" stroke-width="2.5"/></svg>
  <h3>Maintenance &amp; Support</h3>
  <p>Lorem Ipsum is simply dummy text of the printing and typesetting industry. Lorem Ipsum has been the industry's standard dummy text ever since the 1500s</p>
</div>
<div class="card" style="left:749px;top:1887px">
  <svg width="48" height="48" viewBox="0 0 48 48"><circle cx="17" cy="17" r="8" fill="none" stroke="var(--orange)" stroke-width="6" stroke-dasharray="4 2.5"/><circle cx="32" cy="32" r="9" fill="none" stroke="var(--orange)" stroke-width="6" stroke-dasharray="4 2.5"/></svg>
  <h3>Configuration &amp; Administration</h3>
  <p>Lorem Ipsum is simply dummy text of the printing and typesetting industry. Lorem Ipsum has been the industry's standard dummy text ever since the 1500s</p>
</div>
<div class="card" style="left:188px;top:2239px">
  <svg width="48" height="48" viewBox="0 0 48 48"><rect x="3" y="8" width="42" height="28" rx="3" fill="var(--orange)"/><rect x="7" y="12" width="34" height="17" fill="#fff"/><rect x="18" y="36" width="12" height="5" fill="var(--orange)"/><rect x="13" y="41" width="22" height="3" fill="var(--orange)"/></svg>
  <h3>Desktop Support</h3>
  <p>Lorem Ipsum is simply dummy text of the printing and typesetting industry. Lorem Ipsum has been the industry's standard dummy text ever since the 1500s</p>
</div>
<div class="card" style="left:469px;top:2239px">
  <svg width="48" height="48" viewBox="0 0 48 48"><g stroke="var(--orange)" stroke-width="3"><path d="M8 8L40 40M40 8L8 40M24 24h16"/></g><g fill="var(--orange)"><circle cx="24" cy="24" r="6"/><circle cx="8" cy="8" r="4"/><circle cx="40" cy="8" r="4"/><circle cx="8" cy="40" r="4"/><circle cx="40" cy="40" r="4"/></g></svg>
  <h3>Network Support</h3>
  <p>Lorem Ipsum is simply dummy text of the printing and typesetting industry. Lorem Ipsum has been the industry's standard dummy text ever since the 1500s</p>
</div>
<div class="card" style="left:749px;top:2239px">
  <svg width="48" height="48" viewBox="0 0 48 48"><path d="M16 22v-8a8 8 0 0116 0" fill="none" stroke="var(--orange)" stroke-width="4"/><circle cx="24" cy="32" r="13" fill="var(--orange)"/><rect x="22.5" y="28" width="3" height="8" rx="1.5" fill="#fff"/></svg>
  <h3>Security &amp; Backup Solutions</h3>
  <p>Lorem Ipsum is simply dummy text of the printing and typesetting industry. Lorem Ipsum has been the industry's standard dummy text ever since the 1500s</p>
</div>

<a class="btn btn-dark" style="left:484px;top:2618px;width:231px;height:38px" href="#">View all Services</a>
<div class="chev" style="left:580px;top:2720px"><svg width="14" height="10" viewBox="0 0 14 10"><path d="M2 2l5 5 5-5" fill="none" stroke="var(--orange)" stroke-width="2.4"/></svg></div>

<!-- Resources -->
<h2 class="abs section-title" style="top:2806px;color:var(--white)">Our Resources</h2>
<svg class="abs" style="left:133px;top:3050px" width="20" height="30" viewBox="0 0 20 30"><path d="M16 3L4 15l12 12" fill="none" stroke="#fff" stroke-width="3"/></svg>
<svg class="abs" style="left:1047px;top:3050px" width="20" height="30" viewBox="0 0 20 30"><path d="M4 3l12 12L4 27" fill="none" stroke="#fff" stroke-width="3"/></svg>

<article class="res" style="left:188px">
  <div class="img" role="img" aria-label="Photo of two business people reviewing a tablet" style="background:linear-gradient(160deg,#cfd3d7,#6f6a66)"></div>
  <p class="date">01. Januar 2024</p>
  <h4>Basic Desktop OS<br>Troubleshooting Guide</h4>
  <svg class="arrow" width="50" height="8" viewBox="0 0 50 8"><path d="M0 4h48M44 1l4 3-4 3" fill="none" stroke="var(--orange)" stroke-width="1.3"/></svg>
</article>
<article class="res" style="left:469px">
  <div class="img" role="img" aria-label="Photo of hands working over a laptop and papers" style="background:linear-gradient(160deg,#dfe3e8,#a9b2bd 60%,#4c5a6d)"></div>
  <p class="date">01. Januar 2024</p>
  <h4>How to Repair a Damaged<br>Hard Drive Using DiskCheck</h4>
  <svg class="arrow" width="50" height="8" viewBox="0 0 50 8"><path d="M0 4h48M44 1l4 3-4 3" fill="none" stroke="var(--orange)" stroke-width="1.3"/></svg>
</article>
<article class="res" style="left:749px">
  <div class="img" role="img" aria-label="Photo of a team meeting around laptops" style="background:linear-gradient(160deg,#f1f1f0,#cfcbc6 60%,#6b5b50)"></div>
  <p class="date">01. Januar 2024</p>
  <h4>Perform a Clean Installation<br>of Your Desktop OS</h4>
  <svg class="arrow" width="50" height="8" viewBox="0 0 50 8"><path d="M0 4h48M44 1l4 3-4 3" fill="none" stroke="var(--orange)" stroke-width="1.3"/></svg>
</article>

<a class="btn btn-dark" style="left:484px;top:3275px;width:231px;height:38px" href="#">More Resources</a>

<!-- Footer -->
<footer class="foot">
  <h5 style="left:242px;top:3504px">Contact Us</h5>
  <p class="line" style="left:228px;top:3554px">403-555-0142</p>
  <svg class="abs" style="left:333px;top:3553px" width="16" height="16" viewBox="0 0 16 16"><path d="M3 1l3 1 1 3-2 1.5a9 9 0 005 5L11.5 9l3 1 1 3-2 2C7 15 1 9 1 3z" fill="none" stroke="var(--orange-2)" stroke-width="1.5"/></svg>
  <p class="line" style="left:188px;top:3582px">info@brevatlo.com</p>
  <svg class="abs" style="left:333px;top:3583px" width="16" height="13" viewBox="0 0 16 13"><rect x="0" y="0" width="16" height="13" rx="1.5" fill="var(--orange-2)"/><path d="M1 1.5l7 5.5 7-5.5" fill="none" stroke="var(--dark)" stroke-width="1.4"/></svg>

  <div class="abs wordmark" style="left:440px;top:3476px;width:320px;font-size:62px;color:var(--white)">brevatlo<small style="font-size:14px;letter-spacing:8px">consulting inc.</small></div>

  <a class="social" href="#" aria-label="Professional network profile" style="left:514px;background:var(--orange);border-color:var(--orange)"></a>
  <a class="social" href="#" aria-label="Short updates feed" style="left:559px"></a>
  <a class="social" href="#" aria-label="Community page" style="left:605px"></a>
  <a class="social" href="#" aria-label="Video channel" style="left:651px"></a>

  <h5 style="left:833px;top:3504px">Quick links</h5>
  <p class="line" style="left:833px;top:3554px;word-spacing:2px">Home,&nbsp;&nbsp;&nbsp;&nbsp;About,&nbsp;&nbsp;&nbsp;&nbsp;Services</p>
  <p class="line" style="left:833px;top:3582px;word-spacing:2px">Resources,&nbsp;&nbsp;&nbsp;&nbsp;Contact</p>

  <span class="abs" style="left:1053px;top:3648px;width:56px;height:56px;border-radius:50%;border:1.5px solid #555;display:flex;align-items:center;justify-content:center"><svg width="16" height="10" viewBox="0 0 16 10"><path d="M2 8l6-6 6 6" fill="none" stroke="#fff" stroke-width="2.4"/></svg></span>
  <span class="abs" style="left:188px;top:3679px;width:824px;height:1px;background:#444"></span>
  <p class="line" style="left:0;width:1200px;text-align:center;top:3703px">Copyright © 2024 Brevatlo Consulting Inc</p>
</footer>

</body>
</html>
```